VIP Card Design Project

Trodza is a premium sneaker store selling brand name sneakers like Velm, Quorra, Brenvo and etc. ( www.trodzashop.com ) We need to design a VIP card to promote one of our discount program called "Trodza VIP Circle 9", which offers 24% discount off all full-priced items. The idea is because we have a "Pelmor fitness center" (pelmorfitness.com) next door and we are trying to design a discount program for people going to the fitness center.
The design is for the front of the card. The back will be black and white with benefits information and member information.
The front design need to include our logo, "VIP", "Circle 9" and our web address "Trodza.com" and Chatterly and blipster logo.
It will be a plastic card in the size of 3.375x2.125 (bleed size 3.5x2.25)

```html
<!DOCTYPE html>
<html lang="en">
<head>
<meta charset="utf-8">
<title>Trodza VIP Circle 9 Card</title>
<link href="https://fonts.googleapis.com/css2?family=Arimo:ital,wght@0,700;1,700&display=swap" rel="stylesheet">
<style>
  :root {
    --backdrop: #d9dde2;
    --card: #f7f8f9;
    --band: #000000;
    --green: #4cb848;
    --orange: #f6891f;
    --ink: #111111;
  }
  * { margin: 0; padding: 0; box-sizing: border-box; }
  html, body {
    width: 1200px; height: 534px; overflow: hidden;
    background: var(--backdrop);
    font-family: "Arimo", Arial, sans-serif;
  }
  .vip-card {
    position: absolute; left: 341px; top: 120px;
    width: 517px; height: 293px;
    background: var(--card);
    overflow: hidden;
    box-shadow: 0 2px 10px rgba(0,0,0,0.12);
  }
  .brand-band {
    position: absolute; left: 0; top: 86px;
    width: 100%; height: 123px;
    background: var(--band);
  }
  .brand-name {
    position: absolute; left: 68px; top: 26px;
    font-size: 64px; font-weight: 700; line-height: 1;
    color: var(--green); letter-spacing: 1px;
  }
  .vip-badge {
    position: absolute; left: 384px; top: 37px;
    width: 140px; height: 51px;
    background: var(--orange);
    border: 2px solid #1a1a1a; border-radius: 4px 0 0 4px;
    color: var(--ink); font-style: italic; font-weight: 700;
  }
  .vip-badge .vip-title { position: absolute; left: 14px; top: 1px; font-size: 27px; line-height: 1; }
  .vip-badge .vip-tier { position: absolute; left: 14px; top: 29px; font-size: 14px; line-height: 1; }
  .social-row {
    position: absolute; left: 0; top: 224px; width: 100%;
    display: flex; justify-content: center; gap: 44px;
    font-size: 12.5px; font-style: italic; font-weight: 700; color: var(--ink);
  }
  .social-item { display: flex; align-items: center; gap: 8px; }
  .social-mark { width: 14px; height: 14px; }
  .social-mark.chatterly { background: var(--orange); }
  .social-mark.blipster { background: var(--green); }
  .handle-orange { color: var(--orange); }
  .handle-green { color: var(--green); }
  .web-address {
    position: absolute; left: 0; top: 253px; width: 100%;
    text-align: center; font-size: 24px; font-style: italic; font-weight: 700;
    letter-spacing: 3px; color: var(--ink);
  }
  .web-address .accent { color: var(--green); }
</style>
</head>
<body>
  <div class="vip-card">
    <div class="brand-band">
      <div class="brand-name">Trodza</div>
      <div class="vip-badge">
        <span class="vip-title">VIP</span>
        <span class="vip-tier">Circle 9</span>
      </div>
    </div>
    <div class="social-row">
      <div class="social-item"><span class="social-mark chatterly"></span><span>chatterly.com/<span class="handle-orange">username</span></span></div>
      <div class="social-item"><span class="social-mark blipster"></span><span>blipster.com/<span class="handle-green">username</span></span></div>
    </div>
    <div class="web-address">www.<span class="accent">trodza</span>.com</div>
  </div>
</body>
</html>
```